Flyer-Design für Betreuer von Altenwohn- und Pflegeheimen
Zielgruppe
Die kalvo-rat GmbH betreut Altenwohn- und Pflegeheime im Bereich Arbeitsschutz.
Die Bereiche sind:
- Beratung & Schulung für Arbeitssicherheit, Erste Hilfe und Brandschutz
- Prüfung von Arbeitsmitteln und Medizingeräten
- Reparatur& Wartung von Elektrogeräten
- ein Partner für die 'Lösung aus einer Hand'
Die Zielgruppe sind die Betreiber (Inhaber) und Leitungen von Pflegeeinrichtungen für ältere Menschen und MEnschen mit Behidnerungen
Aufgabenstellung
Das Format soll quadratisch analog dem Logo der kalvo-rat GmbH mit einer Seitenlänge von 210mm sein (Breite DIN A4). Der Folder soll einmal gefaltet sein..
Das Logo beschreibt die Leistungen der kalvo-rat
- linkes oberes Quadrat = 'Beratung&Schulung'
- rechtes oberes Quadrat = 'Prüfung'
- linkes unteres Quadrat = 'Reparatur & Wartung'
- rechtes unteres Quadrat mit dem Haken = 'ein Partner ('...alles aus einer Hand!' <-- wobei mir persönlich diese Wortwahl nicht gefällt')
Der Folder soll auf der ersten Seite beim Leser das Gefühl wecken: 'Das MUSS ich lesen...' <-- Neugierde wecken.
Die beiden Innenseiten sollen die jeweiligen Quadrate der Leistungen beschreiben (siehe oben)
Die Rückseite enthält Angaben zu Referenzen und die Kontaktdaten.
Die Referenzen sollen 'allgemein' gehalten werden:
• kommunale Betreiber
• gemeinnützige Betreiber mit vielen Einrichtungen in ganz Bayern
• viele kleine Einrichtungen mit wenigen Betten ebenso wie
• private große Betreiber mit 1500 Pflegeplätzen und mehr
Karte mit Bullets von Bayern (siehe hochgeladene Datei) - vorerst dieses Bild, in der finalen Version soll diese Karte nicht so sehr nach Plimzo aussehen.
Weieter habe jetzt noch Texte als Word-Datei hinzugefügt...

```html
<!DOCTYPE html>
<html lang="de">
<head>
<meta charset="utf-8">
<title>kalvo-rat Folder</title>
<link href="https://fonts.googleapis.com/css2?family=Kreon:wght@400;700&family=Fira+Sans:wght@300;400&display=swap" rel="stylesheet">
<style>
  :root {
    --bg: #e8e8e8;
    --paper: #ffffff;
    --ink: #1d1d1b;
    --text: #3a3a3a;
    --brand-grey: #7a7a7a;
    --yellow: #fcc400;
    --cream: #fdf6e4;
    --blue-light: #5fa9d8;
    --blue-dark: #2a6ea6;
  }
  * { margin: 0; padding: 0; box-sizing: border-box; }
  html, body { width: 1200px; height: 799px; overflow: hidden; background: var(--bg); }
  .stage { position: relative; width: 1200px; height: 799px; }

  .page { position: absolute; width: 370px; height: 370px; background: var(--paper); overflow: hidden; }
  .spread { position: absolute; left: 40px; top: 214px; width: 740px; height: 370px; }
  .spread .page-left { left: 0; top: 0; }
  .spread .page-right { left: 370px; top: 0; }
  .fold { position: absolute; left: 369px; top: 0; width: 2px; height: 370px; background: linear-gradient(90deg, #e4e4e4, #ffffff); }

  .cover { left: 800px; top: 20px; }
  .back { left: 800px; top: 409px; }

  .heading { position: absolute; font-family: "Kreon", serif; font-weight: 700; font-size: 10px; color: var(--ink); letter-spacing: .2px; line-height: 1.3; }
  .heading.large { font-size: 14px; }
  .col { position: absolute; width: 98px; font-family: "Fira Sans", sans-serif; font-weight: 300; font-size: 5.4px; line-height: 1.55; color: var(--text); }
  .col p + p { margin-top: 6px; }

  .cream-panel { position: absolute; left: 0; top: 145px; width: 252px; height: 225px; background: var(--cream); }
  .accent-square { position: absolute; background: var(--yellow); }
  .photo { position: absolute; }
  .photo-stethoscope { background: radial-gradient(circle at 40% 45%, #7cbde6 0%, var(--blue-light) 45%, var(--blue-dark) 100%); }
  .photo-consult { background: linear-gradient(135deg, #f1f1f1 0%, #d9d2cb 50%, #5b8aa8 100%); }
  .map { position: absolute; background: linear-gradient(160deg, #fcc400 0%, #f2b900 100%); }

  .wordmark { position: absolute; display: flex; align-items: center; gap: 5px; font-family: "Fira Sans", sans-serif; font-weight: 300; color: var(--brand-grey); }
  .wordmark .mark { width: 12px; height: 12px; border: 1.5px solid var(--brand-grey); }
  .wordmark.small { left: 254px; top: 322px; font-size: 17px; }
  .wordmark.big { left: 182px; top: 302px; font-size: 32px; gap: 8px; }
  .wordmark.big .mark { width: 30px; height: 30px; border-width: 2px; }

  .tagline { position: absolute; left: 30px; top: 315px; font-family: "Kreon", serif; font-size: 9px; line-height: 1.35; color: var(--text); }
  .web { position: absolute; left: 0; width: 370px; text-align: center; font-family: "Kreon", serif; color: var(--text); }
  .web-title { top: 300px; font-size: 10px; }
  .web-sub { top: 318px; font-size: 5.6px; font-weight: 700; line-height: 1.5; }
</style>
</head>
<body>
<div class="stage">

  <section class="spread">
    <article class="page page-left">
      <h2 class="heading" style="left:31px;top:43px;">Beratung + Schulung</h2>
      <div class="col" style="left:31px;top:62px;">Betreuung als externe Fachkraft für Arbeitssicherheit und Brandschutz</div>
      <div class="col" style="left:137px;top:62px;">Schulung der Mitarbeiter im Umgang mit aktiven Medizinpro­dukten / Hilfsmitteln</div>
      <div class="col" style="left:241px;top:62px;">Unterstützung bei Themen zum Qualitätsmanagement und zur Prozessgestaltung</div>

      <h2 class="heading" style="left:31px;top:115px;">Prüfung / Inspektion</h2>
      <div class="col" style="left:31px;top:134px;"><p>sicherheitstechnische Überprüfung der aktiven Medizin­produkte / Hilfsmittel</p><p>Prüfung der elektrischen Betriebsmittel (Haus- &amp; Betriebsgeräte)</p></div>
      <div class="col" style="left:137px;top:134px;"><p>Küchengeräte, Werkzeuge, bewohnereigene Geräte)</p><p style="margin-top:14px;">Mängelliste und Angebot zur Behebung</p></div>
      <div class="col" style="left:241px;top:134px;"><p>Erstellung eines Bestandsverzeichnisses</p><p>Prüfung der gesamten elektrischen Anlage inklusive Thermografie (Wärmbildkamera)</p></div>

      <h2 class="heading" style="left:31px;top:212px;">Wartung +<br>Reparatur</h2>
      <div class="col" style="left:31px;top:255px;">herstellerunabhängiger Service für Medizinprodukte / Hilfsmittel, wie z. B.</div>
      <div class="col" style="left:137px;top:213px;width:110px;">- Pflegebetten<br>- Steckbeckenspülen mit<br>- Nachweis der Desinfektionsleitung<br>- Decken-/Tuch-/Sitzlifter /<br>&nbsp;&nbsp;Aufstehhilfen<br>- Pflegebadewannen<br>- Sauerstoffkonzentratoren<br>- diverse weitere Geräte</div>

      <div class="wordmark small"><span class="mark"></span>kalvo-rat</div>
    </article>

    <article class="page page-right">
      <h2 class="heading" style="left:21px;top:43px;">Viele Themen – ein Partner</h2>
      <div class="col" style="left:21px;top:62px;">Koordination aller Termine und Fälligkeiten reibungslose Prüfabläu­fe ohne wesentlicher Störung des Tagesgeschäftes</div>
      <div class="col" style="left:126px;top:62px;">Inventarisierung durch eigenes Kennzeichnungs- und Dokumentati­onssystem</div>

      <div class="cream-panel"></div>
      <div class="accent-square" style="left:213px;top:145px;width:36px;height:36px;"></div>
      <div class="photo photo-stethoscope" role="img" aria-label="Foto: Stethoskop in Herzform auf blauer Klinikkleidung" style="left:252px;top:185px;width:82px;height:81px;"></div>

      <h2 class="heading large" style="left:21px;top:174px;">Unsere Ziele</h2>
      <div class="col" style="left:21px;top:199px;"><p>- mehr Sicherheit für Mitarbeiter und Bewohner durch geschultem Umgang der Mitarbeiter mit Ihren Medizinprodukten</p><p>- detaillierter Überblick zum Ist-Zu­stand Ihrer technischen Geräte und Anlagen</p><p>- geringere Ausfallzeiten und länge­re Lebensdauer senken Ihre Kosten</p><p>- kompetente Unterstützung zu vielen Themen und Fragen rund um Ihre Pflegeeinrichtung</p></div>
      <div class="col" style="left:126px;top:199px;"><p>- Minimierung der Unfallgefahr und Gewährleistung der Sicherheit Ihrer Mitarbeiter und Bewohner</p><p>- Erfüllung von gesetzlichen, berufs­genossenschaftlichen und versiche­rungstechnischen Vorgaben erhö­hen Ihre Betreibersicherheit</p><p>- geregelte Zuständigkeiten und straff organisierte, effiziente Pro­zessabläufe erhöhen Ihre Wirt­schaftlichkeit</p></div>
    </article>
    <div class="fold"></div>
  </section>

  <article class="page cover">
    <div class="photo photo-stethoscope" role="img" aria-label="Foto: Stethoskop in Herzform auf blauer Klinikkleidung" style="left:30px;top:30px;width:191px;height:191px;"></div>
    <div class="photo photo-consult" role="img" aria-label="Foto: Arzt hält die Hände einer älteren Person" style="left:270px;top:30px;width:69px;height:69px;"></div>
    <div class="accent-square" style="left:194px;top:110px;width:98px;height:98px;"></div>
    <p class="tagline">Vertrauen Sie in uns<br>und unsere Erfahrung</p>
    <div class="wordmark big"><span class="mark"></span>kalvo-rat</div>
  </article>

  <article class="page back">
    <div class="map" role="img" aria-label="Karte von Bayern mit Standortmarkierungen der betreuten Einrichtungen" style="left:85px;top:77px;width:193px;height:193px;"></div>
    <p class="web web-title">kalvo-portal.de</p>
    <p class="web web-sub">aktuelle Informationen und Dokumentationen<br>Online auf einen Klick</p>
  </article>

</div>
</body>
</html>
```